Online Course Page

We are building a video based online course page. This project is for only the actual page that the student will watch the videos at. They will watch one vide at a time. Once one video lesson is completed then they can move to the next video lesson. The page will need to show the video player. (Main feature.) The list of lessons in the course. Instructor information. Profile picture and bio of the instructor. A Live chat button that will initiate a chat in real-time with the instructor.

The winning designer will also be asked to to design the dashboard area and other aspects of the user interface as an additional project.

Target Market(s)

Adults

Number of Pages Required

1 page

Colors
9bcb3c

Requirements
Must have
• Our logo is attached. Green and grey are our colors. Should feel modern, clean and be simple to navigate. The site will be responsive so the layout should work well on mobile devices.

```html
<!DOCTYPE html>
<html lang="en">
<head>
<meta charset="utf-8">
<title>Lesson – LearnHarbor</title>
<link rel="stylesheet" href="https://fonts.googleapis.com/css2?family=Montserrat:wght@400;500;700;800&family=Noto+Serif:wght@400&display=swap">
<style>
:root{
  --green:#9bcb3c;
  --slate:#2f373b;
  --slate-dark:#272d31;
  --ink:#1e1e1e;
  --rule:#c9c9c9;
  --white:#ffffff;
}
*{box-sizing:border-box;margin:0;padding:0}
html,body{width:1033px;height:1200px;overflow:hidden;background:var(--white);font-family:"Montserrat",sans-serif;color:var(--ink)}
.page{position:relative;width:1033px;height:1200px}
.abs{position:absolute}

.topbar{left:0;top:0;width:1033px;height:61px;background:var(--slate)}
.brand{display:flex;align-items:center;gap:6px;color:var(--white);font-weight:700;font-size:16px}
.brand .dot{width:14px;height:14px;border-radius:50%;background:var(--green)}
.topbar .brand{left:111px;top:20px}
.mainnav{top:23px;color:var(--white);font-size:14px;font-weight:500;letter-spacing:.2px}
.search{left:905px;top:22px}

.player{left:180px;top:75px;width:673px;height:299px;background:var(--slate)}
.player-frame{left:253px;top:75px;width:531px;height:299px;background:linear-gradient(100deg,#5d4331 0%,#7a5a40 45%,#3e3a38 100%)}
.play-btn{left:494px;top:202px;width:45px;height:45px;border-radius:50%;background:var(--green)}
.progress{left:262px;top:342px;width:513px;height:3px;background:rgba(255,255,255,.35)}
.progress i{display:block;width:6px;height:3px;background:#e52d27}
.controls{left:262px;top:350px;width:513px;height:18px}
.time{left:363px;top:352px;color:var(--white);font-size:10px;font-weight:500}
.nav-arrow{top:214px}

.lesson-title{left:181px;top:384px;font-size:23px;font-weight:400}
.bio-head{left:180px;top:432px;font-size:22px;color:var(--green);font-weight:400}
.bio-text{left:180px;top:468px;width:470px;font-family:"Noto Serif",serif;font-size:9.8px;line-height:14.5px;color:#222}
.portrait{left:716px;top:423px;width:137px;height:176px;border:1px solid #333;border-radius:5px;background:linear-gradient(180deg,#f2f2f2 0%,#d8d2cc 55%,#36476a 100%)}
.chat-btn{left:716px;top:604px;width:137px;height:31px;background:var(--green);color:var(--white);font-size:10.5px;font-weight:700;display:flex;align-items:center;justify-content:center}
.divider{left:180px;top:646px;width:673px;height:1px;background:var(--rule)}

.curriculum-head{left:180px;top:656px;font-size:23px;font-weight:700;color:var(--green)}
.lessons{left:180px;top:690px;list-style:none;font-size:19.5px;line-height:30.7px;letter-spacing:.3px}

.footer{left:0;top:923px;width:1033px;height:215px;background:var(--slate);color:var(--white)}
.col-head{font-size:13px;font-weight:700;letter-spacing:.3px;top:939px;color:var(--white)}
.categories{left:111px;top:966px;list-style:none;color:var(--white);font-size:13px;line-height:28.2px}
.code-input{left:317px;top:960px;width:206px;height:33px;border:1px solid #1b1f22;color:#6f767a;font-size:11.5px;padding:9px 4px}
.validate{left:317px;top:1003px;width:112px;height:31px;background:var(--green);color:var(--white);font-weight:700;font-size:12.5px;display:flex;align-items:center;justify-content:center}
.tag{height:18px;padding:0 5px;background:#1f2427;color:var(--white);font-size:9.5px;font-weight:800;display:flex;align-items:center}

.bottombar{left:0;top:1138px;width:1033px;height:62px;background:var(--slate-dark)}
.bottombar .brand{left:111px;top:1160px;font-size:13px}
.bottombar .brand .dot{width:12px;height:12px}
.footnav{top:1162px;color:var(--white);font-size:13px;font-weight:700;letter-spacing:.3px}
</style>
</head>
<body>
<div class="page">

  <header class="abs topbar"></header>
  <div class="abs brand"><span class="dot"></span>LearnHarbor</div>
  <nav>
    <span class="abs mainnav" style="left:510px">ALL COURSES</span>
    <span class="abs mainnav" style="left:641px">ALL INSTRUCTORS</span>
    <span class="abs mainnav" style="left:803px">ARTICLES</span>
  </nav>
  <svg class="abs search" width="16" height="16" viewBox="0 0 16 16" fill="none" stroke="#fff" stroke-width="2"><circle cx="7" cy="7" r="5.2"/><path d="M11 11l4 4"/></svg>

  <section class="abs player"></section>
  <div class="abs player-frame" role="img" aria-label="Video thumbnail: course introduction with the instructor"></div>
  <div class="abs play-btn"><svg width="45" height="45" viewBox="0 0 45 45"><path d="M18 14l13 8.5L18 31z" fill="#fff"/></svg></div>
  <div class="abs progress"><i></i></div>
  <svg class="abs controls" viewBox="0 0 513 18" fill="#fff">
    <path d="M13 3l10 6-10 6z"/>
    <path d="M46 4l8 5-8 5z"/><rect x="55" y="4" width="2" height="10"/>
    <path d="M80 7h3l4-4v12l-4-4h-3z"/><path d="M89 6q3 3 0 6" stroke="#fff" fill="none" stroke-width="1.3"/>
    <rect x="458" y="4" width="16" height="10" rx="1" fill="none" stroke="#fff" stroke-width="1.6"/>
    <circle cx="491" cy="9" r="4.5" fill="none" stroke="#fff" stroke-width="3" stroke-dasharray="2 1.5"/>
    <path d="M500 3h4M500 3v4M512 3h-4M512 3v4M500 15h4M500 15v-4M512 15h-4M512 15v-4" stroke="#fff" stroke-width="1.8"/>
    <rect x="400" y="4" width="14" height="10" rx="1.5"/>
    <rect x="428" y="8" width="8" height="2"/>
  </svg>
  <span class="abs time">0:09 / 11:45</span>
  <svg class="abs nav-arrow" style="left:143px" width="26" height="24" viewBox="0 0 26 24" fill="none" stroke="#9bcb3c" stroke-width="3"><path d="M24 12H3M12 3l-9 9 9 9"/></svg>
  <svg class="abs nav-arrow" style="left:864px" width="26" height="24" viewBox="0 0 26 24" fill="none" stroke="#9bcb3c" stroke-width="3"><path d="M2 12h21M14 3l9 9-9 9"/></svg>

  <h1 class="abs lesson-title">Title of Lesson</h1>
  <h2 class="abs bio-head">Bio</h2>
  <p class="abs bio-text">Excepteur sint occaecat cupidatat non proident, sunt in culpa qui officia deserunt mollit anim id est eopksio laborum. Sed ut perspiciatis unde omnis istpoe natus error sit voluptatem accusantium doloremque eopsloi laudantium, totam rem aperiam, eaque ipsa quae ab illo inventore veritatis et quasi architecto beatae vitae dicta sunot explicabo. Nemo ernim ipsam voluptatem quia voluptas sit aspernatur aut odit aut fugit, sedopk quia consequuntur magni dolores eos qui rationesopl voluptatem sequi nesciunt. Neque porro quisquameo est, qui dolorem ipsum quia dolor sit amet, eopsmiep consectetur, adipisci velit, seisud quia non numquam eius modi tempora incidunt ut labore et dolore wopeir magnam aliquam quaerat voluptatem eoplmuriquisqu</p>
  <div class="abs portrait" role="img" aria-label="Instructor profile photo"></div>
  <div class="abs chat-btn">CHAT WITH JOHN DOE</div>
  <div class="abs divider"></div>

  <h2 class="abs curriculum-head">Curriculum</h2>
  <ol class="abs lessons">
    <li>1.&nbsp; lesson one</li>
    <li>2. lesson two</li>
    <li>3. lesson three</li>
    <li>4. lesson four</li>
    <li>5. lesson five</li>
    <li>6. lesson six</li>
    <li>7.&nbsp; lesson seven</li>
  </ol>

  <footer class="abs footer"></footer>
  <h3 class="abs col-head" style="left:111px">COURSE CATEGORIES</h3>
  <ul class="abs categories">
    <li>Employment</li><li>Consulting</li><li>BCBA</li><li>Autism</li><li>Asperger's Syndrome</li>
  </ul>
  <h3 class="abs col-head" style="left:317px">CERTIFICATE CODE</h3>
  <div class="abs code-input">Enter Cerificate Code</div>
  <div class="abs validate">VALIDATE</div>
  <h3 class="abs col-head" style="left:579px">TAGS</h3>
  <span class="abs tag" style="left:579px;top:974px">504</span>
  <span class="abs tag" style="left:620px;top:974px">ABA</span>
  <span class="abs tag" style="left:662px;top:974px">APSE</span>
  <span class="abs tag" style="left:711px;top:974px">FAPE</span>
  <span class="abs tag" style="left:761px;top:974px">IDEA</span>
  <span class="abs tag" style="left:579px;top:1002px">INDIVIDUALIZED EDUCATION</span>
  <span class="abs tag" style="left:579px;top:1030px">PROGRAM</span>
  <span class="abs tag" style="left:579px;top:1055px">WEBINAR</span>

  <div class="abs bottombar"></div>
  <div class="abs brand" style="left:111px;top:1160px;font-size:13px"><span class="dot" style="width:12px;height:12px"></span>LearnHarbor</div>
  <span class="abs footnav" style="left:592px">HOME</span>
  <span class="abs footnav" style="left:671px">ABOUT</span>
  <span class="abs footnav" style="left:758px">BLOG</span>
  <span class="abs footnav" style="left:834px">CONTACT US</span>
</div>
</body>
</html>
```